Anzeigengestaltung für Immobilienmakler
Zielgruppe
Wir sind ein Immobilienmakler. Wir wollen eine Plakatkampagne starten. Dazu brauchen wir ein Plakat.
Ich habe noch ein Foto des Plakats hochgeladen, um die Situation zu verdeutlichen.
Aufgabenstellung
Die Maße sind als Anhang dabei. Außerdem dabei ist ein Beispiel eines unserer Werbeschilder (daraus bitte die Farbgebung übernehmen), sowie unser Logo.
Das Plakat sollte mit einem Spruch sein, gerne mit Witz, pfiffig - einfach ein Hingucker.

```html
<!DOCTYPE html>
<html lang="de">
<head>
<meta charset="utf-8">
<title>Plakat – Anna Brecht Immobilien</title>
<link rel="stylesheet" href="https://fonts.googleapis.com/css2?family=Montserrat:wght@800&family=Cormorant+Garamond:wght@500&display=swap">
<style>
  :root {
    --paper: #ffffff;
    --sky-top: #23528a;
    --sky-mid: #4d7fbf;
    --horizon: #6f94c4;
    --hills: #4f6f8f;
    --village: #b88a6e;
    --field-light: #5aa332;
    --field-mid: #3f8a2a;
    --field-dark: #1d5a2a;
    --white: #ffffff;
    --frame: rgba(200, 200, 200, 0.85);
  }
  html, body {
    margin: 0;
    padding: 0;
    width: 1200px;
    height: 835px;
    overflow: hidden;
    background: var(--paper);
  }
  .poster {
    position: relative;
    width: 1200px;
    height: 835px;
    background: var(--paper);
  }
  .landscape {
    position: absolute;
    left: 18px; top: 18px;
    width: 1167px; height: 794px;
    background: linear-gradient(180deg,
      var(--sky-top) 0%,
      var(--sky-mid) 30%,
      var(--horizon) 44%,
      var(--hills) 50%,
      var(--village) 56%,
      var(--field-light) 62%,
      var(--field-mid) 78%,
      var(--field-dark) 100%);
  }
  .frame {
    position: absolute;
    left: 33px; top: 37px;
    width: 1134px; height: 746px;
    border: 2px solid var(--frame);
    border-bottom: none;
    box-sizing: border-box;
  }
  .frame-base {
    position: absolute;
    height: 2px;
    top: 782px;
    background: var(--frame);
  }
  .frame-base--left { left: 33px; width: 657px; }
  .frame-base--right { left: 1110px; width: 57px; }
  .headline {
    position: absolute;
    left: 70px; top: 62px;
    margin: 0;
    font-family: "Montserrat", sans-serif;
    font-weight: 800;
    font-size: 96px;
    line-height: 98px;
    letter-spacing: 1px;
    color: var(--white);
  }
  .pointer {
    position: absolute;
    left: 540px; top: 395px;
    width: 280px; height: 150px;
  }
  .answer {
    position: absolute;
    left: 82px; top: 556px;
    margin: 0;
    font-family: "Cormorant Garamond", serif;
    font-weight: 500;
    font-size: 76px;
    line-height: 83px;
    letter-spacing: 1px;
    color: var(--white);
  }
  .website {
    position: absolute;
    left: 82px; top: 716px;
    font-family: "Cormorant Garamond", serif;
    font-weight: 500;
    font-size: 41px;
    line-height: 1.2;
    color: var(--white);
  }
  .brand {
    position: absolute;
    left: 740px; top: 706px;
    width: 360px;
    margin: 0;
    text-align: center;
    font-family: "Cormorant Garamond", serif;
    font-weight: 500;
    font-size: 38px;
    line-height: 40px;
    color: var(--white);
  }
</style>
</head>
<body>
  <main class="poster">
    <div class="landscape" role="img" aria-label="Landschaftsfoto: Dorf mit roten Dächern und Kirchturm vor blauen Bergen, grüne Wiese im Vordergrund, Obstbaum rechts, blauer Himmel"></div>
    <div class="frame"></div>
    <div class="frame-base frame-base--left"></div>
    <div class="frame-base frame-base--right"></div>

    <h1 class="headline">HOSCHT A HÄUSLE<br>ZOM VERKAUFA?</h1>

    <svg class="pointer" viewBox="0 0 280 150" aria-hidden="true">
      <path d="M190 40 C 150 20, 170 0, 210 5 C 250 10, 262 45, 240 68 C 215 90, 170 80, 180 45 C 150 55, 70 90, 25 125"
            fill="none" stroke="#ffffff" stroke-width="5" stroke-linecap="round"/>
      <path d="M22 105 L 22 128 L 46 130" fill="none" stroke="#ffffff" stroke-width="5" stroke-linecap="round" stroke-linejoin="round"/>
    </svg>

    <p class="answer">KOI PROBLEM -<br>MIR HELFED DR!</p>
    <div class="website">www.abrecht-immobilien.de</div>

    <p class="brand">Anna Brecht<br>Immobilien</p>
  </main>
</body>
</html>
```